International Shipping Company requires business card designs

We are a company based in Dubai UAE with our core business being shipping and container services. Our details can be found at www.coralwakefreight.com

We are not looking for a design that necessarily involves "ships or other shipping pictures", although some reference to the business in design or colour is encouraged.

Overall design of the card must be smart and depict the company which is very professional. Fonts, colours and layout must be very contemporary in look.

Shipping

```html
<!DOCTYPE html>
<html lang="en">
<head>
<meta charset="utf-8">
<title>Coral Wake International Shipping – Business Cards</title>
<link rel="stylesheet" href="https://fonts.googleapis.com/css2?family=Arimo:ital,wght@0,400;0,700&display=swap">
<style>
  :root {
    --page-bg: #e6e8eb;
    --card-bg: #ffffff;
    --navy: #2b2f86;
    --ocean: #1f7ec4;
    --ink: #2e2e2e;
    --muted: #4a4a4a;
  }
  * { box-sizing: border-box; margin: 0; padding: 0; }
  html, body {
    width: 1200px; height: 951px; overflow: hidden;
    background: var(--page-bg);
    font-family: "Arimo", Arial, sans-serif;
    color: var(--ink);
  }
  .canvas { position: relative; width: 1200px; height: 951px; }

  .card {
    position: absolute;
    width: 640px; height: 366px;
    background: var(--card-bg);
    border-radius: 22px;
    box-shadow: 0 10px 28px rgba(0,0,0,0.18);
    overflow: hidden;
  }
  .card--front { left: 70px; top: 60px; }
  .card--back  { left: 490px; top: 520px; }

  .brand { position: absolute; display: flex; align-items: center; gap: 16px; }
  .brand__dot {
    flex: none; border-radius: 50%; background: var(--navy);
  }
  .brand__name {
    color: var(--ocean); font-weight: 700; text-transform: uppercase;
    line-height: 1.05; letter-spacing: 0.5px;
  }
  .brand__name span { display: block; }

  .card--front .brand { left: 56px; top: 120px; }
  .card--front .brand__dot { width: 76px; height: 76px; }
  .card--front .brand__main { font-size: 44px; }
  .card--front .brand__sub { font-size: 19px; }

  .front__url {
    position: absolute; left: 128px; top: 276px;
    font-size: 19px; letter-spacing: 1.5px; color: var(--ink);
  }

  .back__swoosh { position: absolute; inset: 0; width: 100%; height: 100%; }

  .card--back .brand { left: 228px; top: 66px; }
  .card--back .brand__dot { width: 58px; height: 58px; }
  .card--back .brand__main { font-size: 34px; }
  .card--back .brand__sub { font-size: 15px; }

  .person { position: absolute; left: 44px; top: 170px; }
  .person__name { font-size: 22px; color: var(--ink); }
  .person__role { font-size: 16px; color: var(--ocean); margin-top: 2px; }

  .address {
    position: absolute; left: 44px; top: 246px;
    font-size: 18px; line-height: 1.35; color: var(--muted); font-style: normal;
  }

  .contacts { position: absolute; left: 268px; top: 236px; list-style: none; }
  .contacts li {
    display: flex; align-items: center; gap: 10px;
    font-size: 17px; line-height: 1.3; color: var(--muted);
  }
  .contacts svg { width: 15px; height: 15px; flex: none; fill: var(--ocean); }
</style>
</head>
<body>
<main class="canvas">

  <section class="card card--front" aria-label="Business card front">
    <div class="brand">
      <span class="brand__dot"></span>
      <p class="brand__name">
        <span class="brand__main">Coral Wake</span>
        <span class="brand__sub">International Shipping (L.L.C.)</span>
      </p>
    </div>
    <p class="front__url">www.coralwakefreight.com</p>
  </section>

  <section class="card card--back" aria-label="Business card back">
    <svg class="back__swoosh" viewBox="0 0 640 366" preserveAspectRatio="none" aria-hidden="true">
      <path d="M0 0 H120 Q30 30 0 110 Z" fill="var(--ocean)"/>
      <path d="M0 120 Q40 30 150 0 H165 Q55 32 0 140 Z" fill="var(--navy)"/>
      <path d="M640 366 H500 Q600 330 640 230 Z" fill="var(--ocean)"/>
      <path d="M640 215 Q610 320 470 366 H452 Q590 325 640 200 Z" fill="var(--navy)"/>
    </svg>

    <div class="brand">
      <span class="brand__dot"></span>
      <p class="brand__name">
        <span class="brand__main">Coral Wake</span>
        <span class="brand__sub">International Shipping (L.L.C.)</span>
      </p>
    </div>

    <div class="person">
      <p class="person__name">Marcus Hale</p>
      <p class="person__role">director</p>
    </div>

    <address class="address">
      1450 Quay Mist Rd<br>
      Dalton, TX 78410
    </address>

    <ul class="contacts">
      <li>
        <svg viewBox="0 0 16 16" aria-hidden="true"><path d="M4 1 L6.5 4.5 L5 6.5 Q6.5 9.5 9.5 11 L11.5 9.5 L15 12 L13 15 Q6 14 1 3 Z"/></svg>
        512-004-7300
      </li>
      <li>
        <svg viewBox="0 0 16 16" aria-hidden="true"><rect x="2" y="7" width="12" height="6" rx="1"/><rect x="4" y="2" width="8" height="4"/></svg>
        512-004-7301
      </li>
      <li>
        <svg viewBox="0 0 16 16" aria-hidden="true"><path d="M1 4 H15 V13 H1 Z M1 4 L8 9 L15 4" stroke="#fff" stroke-width="1"/></svg>
        info@coralwakefreight.com
      </li>
      <li>
        <svg viewBox="0 0 16 16" aria-hidden="true"><circle cx="8" cy="8" r="7"/></svg>
        www.coralwakefreight.com
      </li>
    </ul>
  </section>

</main>
</body>
</html>
```